Wordpress site for cyber security and network perfomance software vendor

We need a brand new Wordpress website consisting of a single home/landing page and page template so that we can add pages in future.
The website is intended to provide information to prospects and customers. The homepage should have a top menu bar that is customizable similar to what we already have at qelvora.com.
Note that we are after a new design – that is, please don’t reference our existing website for design inspiration (qelvora.com)
We are after a Wordpress site that may be implemented straight onto our Wordpress hoster (HostMarrow) .
Quillmo is a software company delivering a solution for customers to get visibility of network performance and cyber security. The Quillmo solution reduces cyber security risk, identifies performance bottlenecks and ultimately lower costs by reducing the number of tools need to monitor the IT environment
We deliver network performance and cyber security information to the IT manager and network teams in a format that they understand, at a realistic cost, and requiring minimal resource to implement. This is a crowded market, most competitors provide highly complex, expensive and highly customized tools to large enterprise. Quillmo makes this style of visibility tool accessible to the mid market.

Target Market(s)

IT Managers, network engineers, mid market organisations, IT service providers

Industry/Entity Type

IT

Font styles to use
Sans Serif

Colors
0094D4
00A9DD
6FCCEA
C7EBF8
E9F6FB

Requirements
Must have
• Fully coded for WordPress. Responsive and mobile friendly. The website copy is provided in the attached document. Utilise the Quillmo logo colors as part of the design (Dark Blue: 2E4F99, Light Blue: 00AFF4, Green: 73D94F). Top Horizontal menu bar for additional pages. Implement one of our screenshots (I have included a bunch of screenshots to choose from)
Nice to have
• Icons, panels or infographics matching the services. Our existing site is built using Pelk – this is not a requirement for the new site but a nice to have as we are familiar with Pelk.
Should not have
• Preferably no corporate images – business people shaking hands or teams of people a meeting room (or that kind of thing)

```html
<!DOCTYPE html>
<html lang="en">
<head>
<meta charset="utf-8">
<title>Quillmo – Network Performance &amp; Cyber Security</title>
<link href="https://fonts.googleapis.com/css2?family=Montserrat:wght@600;700&family=Roboto:wght@400;500;700&display=swap" rel="stylesheet">
<style>
:root{
  --blue:#00A9DD;
  --blue-deep:#0094D4;
  --navy:#2E4F99;
  --green:#73D94F;
  --green-dark:#7CC142;
  --ice:#E3F2FA;
  --text:#222;
  --muted:#6a6a6a;
  --dark:#181818;
  --white:#fff;
}
*{box-sizing:border-box;margin:0;padding:0}
html,body{width:1200px;height:3683px;overflow:hidden}
body{position:relative;font-family:"Roboto",sans-serif;color:var(--text);background:var(--white)}
.abs{position:absolute}
h1,h2,h3{font-family:"Montserrat",sans-serif}
.btn{position:absolute;display:flex;align-items:center;justify-content:center;border-radius:26px;font:700 15px "Roboto",sans-serif;text-transform:uppercase;letter-spacing:.2px}
.btn-blue{background:var(--blue);color:var(--white)}
.btn-white{background:var(--white);color:var(--blue)}

/* header */
.topline{left:0;top:0;width:1200px;height:4px;background:var(--green)}
.header{left:0;top:4px;width:1200px;height:93px;background:var(--white)}
.brand{display:flex;align-items:center;gap:10px;font:500 32px "Roboto",sans-serif;color:var(--navy)}
.brand-dot{width:44px;height:44px;border-radius:50%;background:var(--green)}
.nav{left:385px;top:38px;display:flex;gap:30px;font:500 15px "Roboto",sans-serif;color:#111}
.login{left:970px;top:28px;width:118px;height:42px;gap:8px;font-size:14px}

/* hero */
.hero{left:0;top:97px;width:1200px;height:653px;background:linear-gradient(120deg,#1d3a82 0%,#2e55b0 45%,#3050a8 70%,#1c2f6e 100%)}
.hero-wave{left:0;top:640px;width:1200px;height:112px}
.hero-title{left:110px;top:322px;width:560px;font:700 23.5px/34px "Montserrat",sans-serif;color:var(--white);white-space:nowrap}
.laptop{left:546px;top:426px;width:544px;height:320px}
.dash{left:598px;top:430px;width:456px;height:300px;border-radius:6px;background:linear-gradient(180deg,#1e2228 0%,#2b3038 100%);border:6px solid #2a2a2e}

/* about */
.about-photo{left:130px;top:843px;width:396px;height:396px;border-radius:50%;background:linear-gradient(135deg,#4b6aa8 0%,#1d2b52 55%,#0f1830 100%);border:8px solid #fff;box-shadow:0 0 0 1px #e2e2e2}
.about-arc{left:108px;top:832px;width:430px;height:430px}
.about-title{left:602px;top:855px;font:700 34px "Montserrat",sans-serif;color:#111}
.about-text{left:602px;top:922px;width:490px;font:400 14px/24px "Roboto",sans-serif;color:var(--muted);text-align:justify}
.about-text p+p{margin-top:20px;text-align:left}

/* services */
.services{left:0;top:1333px;width:1200px;height:841px;background:var(--ice)}
.sec-title{width:1200px;text-align:center;font:700 26px "Montserrat",sans-serif;color:#111}
.card{position:absolute;width:312px;height:282px;background:var(--white);border-radius:6px;box-shadow:0 2px 10px rgba(0,0,0,.06);padding:30px 21px}
.card svg{width:62px;height:62px;display:block}
.card h3{margin-top:24px;font:700 18px/22px "Roboto",sans-serif;color:var(--navy);text-transform:uppercase}
.card p{margin-top:14px;font:400 14px/22px "Roboto",sans-serif;color:var(--muted)}

/* why */
.why{left:0;top:2174px;width:1200px;height:472px;background:linear-gradient(90deg,#1c1c1c 0%,#2a2d31 55%,#202326 100%)}
.why-title{left:112px;top:2225px;font:700 34px "Montserrat",sans-serif;color:var(--white)}
.why-text{left:112px;top:2292px;width:488px;font:400 14px/24px "Roboto",sans-serif;color:#e6e6e6;text-align:justify}
.why-text p+p{margin-top:20px}
.why-mark{left:660px;top:2200px;width:440px;height:420px;border-radius:50%;background:radial-gradient(circle,rgba(80,110,150,.35) 0%,rgba(40,50,60,0) 70%)}

/* blog */
.blog-card{position:absolute;background:var(--white);box-shadow:0 2px 12px rgba(0,0,0,.08)}
.blog-img{position:absolute}
.date{position:absolute;background:var(--green-dark);color:var(--white);font:700 12px "Roboto",sans-serif;padding:8px 14px;text-transform:uppercase}
.blog-card h3{position:absolute;font:500 16px/27px "Roboto",sans-serif;color:#111;text-transform:uppercase;white-space:nowrap}
.blog-card p{position:absolute;font:400 14px/23px "Roboto",sans-serif;color:var(--muted)}

/* footer */
.footer{left:0;top:3343px;width:1200px;height:289px;background:var(--dark);color:var(--white)}
.foot-col h4{font:700 17px "Roboto",sans-serif;text-transform:uppercase;margin-bottom:18px}
.foot-col li{list-style:none;font:400 15px/25px "Roboto",sans-serif}
.contact{display:flex;align-items:center;gap:20px;margin-bottom:20px}
.contact b{display:block;font:700 15px "Roboto",sans-serif}
.contact span{font:400 14px "Roboto",sans-serif}
.bottom{left:0;top:3632px;width:1200px;height:51px;background:var(--green-dark);color:var(--white);font:400 12px "Roboto",sans-serif;display:flex;align-items:center;justify-content:center}
</style>
</head>
<body>

<div class="abs header"></div>
<div class="abs topline"></div>
<div class="abs brand" style="left:112px;top:28px"><span class="brand-dot"></span>quillmo</div>
<nav class="abs nav">
  <span>Home</span><span>Product</span><span>Blog</span><span>About</span><span>Partner Portal</span><span>Contact Us</span>
</nav>
<div class="btn btn-blue login">
  <svg width="16" height="16" viewBox="0 0 16 16"><circle cx="8" cy="8" r="7" fill="none" stroke="#fff" stroke-width="1.5"/><circle cx="8" cy="6.3" r="2.4" fill="#fff"/><path d="M3.6 12.6c1-1.8 2.6-2.6 4.4-2.6s3.4.8 4.4 2.6" fill="#fff"/></svg>Login
</div>

<section>
  <div class="abs hero" role="img" aria-label="Engineer working at computer screens showing network data, in blue tones"></div>
  <svg class="abs hero-wave" viewBox="0 0 1200 112" preserveAspectRatio="none"><path d="M0 68 C160 24 300 -6 470 14 C640 34 760 112 960 94 C1060 84 1140 56 1200 54 L1200 112 L0 112 Z" fill="#fff"/></svg>
  <h1 class="abs hero-title">Specialising in IT Network Performance &amp;<br>Cyber Security Solutions for Small<br>to Medium Organisations.</h1>
  <div class="btn btn-white" style="left:110px;top:450px;width:149px;height:49px">Get Started</div>
  <svg class="abs laptop" viewBox="0 0 544 320"><rect x="44" y="0" width="466" height="310" rx="10" fill="#2a2a2e"/><path d="M0 306 H544 L530 320 H14 Z" fill="#bcbcc0"/><rect x="230" y="306" width="84" height="5" rx="2" fill="#8d8d92"/></svg>
  <div class="abs dash" role="img" aria-label="Product dashboard screenshot with performance charts and bar lists"></div>
</section>

<section>
  <svg class="abs about-arc" viewBox="0 0 430 430"><path d="M215 8 A207 207 0 0 0 215 422" fill="none" stroke="#7CC142" stroke-width="9"/></svg>
  <div class="abs about-photo" role="img" aria-label="Hands typing on a laptop keyboard"></div>
  <h2 class="abs about-title">ABOUT US</h2>
  <div class="abs about-text">
    <p>Quillmo is a complete network monitoring solution providing scalable IT visibility and security monitoring for organisations ranging from SME’s through to large enterprise. Quillmo delivers deep insight into network performance and cyber security incidents to help you regain control of your network ensuring consistent user experience and security.</p>
    <p>Quillmo understands the importance of resolving network and security issues fast. You need more intuitive, lower cost solutions that require less effort to get to the root cause of problems.</p>
  </div>
  <div class="btn btn-blue" style="left:602px;top:1168px;width:152px;height:50px">Learn More</div>
</section>

<section>
  <div class="abs services"></div>
  <h2 class="abs sec-title" style="left:0;top:1415px">WE DELIVER EVERYTHING YOU NEED</h2>

  <div class="card" style="left:112px;top:1504px">
    <svg viewBox="0 0 62 62" fill="none" stroke="#7CC142" stroke-width="2"><rect x="3" y="4" width="56" height="42" rx="2"/><circle cx="34" cy="25" r="10"/><path d="M30 27l3-4 3 3 3-5"/><circle cx="12" cy="52" r="6"/><path d="M12 46V20M18 52h20"/></svg>
    <h3>Sophisticated Data<br>Analytics</h3>
    <p>Powerful data analytics correlate threat data and anomalous traffic data with network performance to deliver meaningful information so you can easily respond.</p>
  </div>
  <div class="card" style="left:444px;top:1504px">
    <svg viewBox="0 0 62 62" fill="none" stroke="#7CC142" stroke-width="2"><rect x="3" y="4" width="56" height="36" rx="2"/><path d="M10 32l8-10 8 6 8-12"/><path d="M40 30v-6M46 30v-10M52 30v-14"/><path d="M22 40l-6 18M40 40l6 18M31 40v18M18 50h26"/></svg>
    <h3>Best Visual<br>Analytics</h3>
    <p>Proactive alerts and dynamic traffic flows are integrated into an intuitive, user friendly dashboard that enable you to plug your visibility blind spots.</p>
  </div>
  <div class="card" style="left:776px;top:1504px">
    <svg viewBox="0 0 62 62" fill="none" stroke="#7CC142" stroke-width="2"><path d="M14 26c-6 0-9-4-9-8s4-8 9-7c1-6 7-9 12-7 3-4 10-4 13 1 5-1 10 3 9 8 4 1 6 5 5 9s-5 5-8 4"/><circle cx="31" cy="32" r="9"/><path d="M31 41v16M25 57h12M23 26l-5-4M39 26l5-4"/></svg>
    <h3>Flexible<br>Solutions</h3>
    <p>Our network monitoring AND cyber security solution can be scaled to fit your organisation.</p>
  </div>
  <div class="card" style="left:278px;top:1806px">
    <svg viewBox="0 0 62 62" fill="none" stroke="#7CC142" stroke-width="2"><circle cx="31" cy="31" r="19"/><path d="M31 4v7M31 51v7M4 31h7M51 31h7M12 12l5 5M45 45l5 5M12 50l5-5M45 17l5-5"/><path d="M21 27l5-6h10l5 6-10 12z M21 27h20M28 21l-2 6 5 12 5-12-2-6"/></svg>
    <h3>Superior<br>Service</h3>
    <p>From first contact through to deployment, our friendly, expert team will discuss your needs and quickly installour easy-to-use platform and tools.</p>
  </div>
  <div class="card" style="left:610px;top:1806px">
    <svg viewBox="0 0 62 62" fill="none" stroke="#7CC142" stroke-width="2"><rect x="8" y="3" width="40" height="56" rx="2"/><rect x="15" y="12" width="26" height="26"/><path d="M15 21h26M15 29h26M24 12v26M14 48h18"/><path d="M42 44c-3 0-4 1.5-4 3s1 2.5 4 3 4 1.5 4 3-1 3-4 3-4-1.5-4-2M42 42v16"/></svg>
    <h3>Decrease Your Total Cost<br>of Ownership</h3>
    <p>Proactive alerts and dynamic traffic flows are integrated into an intuitive, user friendly dashboard that enable you to plug your visibility blind spots.</p>
  </div>
</section>

<section>
  <div class="abs why" role="img" aria-label="Dark background of a person working at a desk"></div>
  <div class="abs why-mark"></div>
  <h2 class="abs why-title">WHY QUILLMO?</h2>
  <div class="abs why-text">
    <p>At Quillmo, we understand the challenges that you face. Cyber security and network incidents can have devastating impacts on small to medium organisations because you typically don’t have the time, staff, or resources to develop complicated responses to cyber security threats.</p>
    <p>That’s why small to medium sized organisations are vulnerable to potentially devastating cyber incidents.Did you know that on average, it took over 220 days for organisations to identify a breach and a further 80 days to contain the breach? (Halvern Security, 2020).</p>
  </div>
  <div class="btn btn-blue" style="left:112px;top:2540px;width:152px;height:50px">Learn More</div>
</section>

<section>
  <h2 class="abs sec-title" style="left:0;top:2736px;font-size:34px">LATEST BLOG</h2>

  <article class="blog-card" style="left:112px;top:2818px;width:477px;height:431px">
    <div class="blog-img" role="img" aria-label="Hand touching a glowing digital security interface" style="left:0;top:0;width:477px;height:274px;background:linear-gradient(135deg,#0e2f6a 0%,#1f6fc0 50%,#0b2552 100%)"></div>
    <span class="date" style="left:39px;top:258px">17 Feb 2021</span>
    <h3 style="left:39px;top:310px">If only we could evaluate and quantify web<br>base application performance ...</h3>
    <p style="left:39px;top:377px;width:425px">Increasingly (or almost exclusively?) applications are delivered<br>via web based single page applications</p>
  </article>

  <article class="blog-card" style="left:609px;top:2818px;width:478px;height:202px">
    <div class="blog-img" role="img" aria-label="Man looking at a tablet in front of blue charts" style="left:0;top:0;width:191px;height:202px;background:linear-gradient(135deg,#4a6fa8 0%,#1e3c7a 60%,#0f2246 100%)"></div>
    <span class="date" style="left:212px;top:22px">22 Dec 2020</span>
    <h3 style="left:212px;top:66px">Will TLS 1.3 split the<br>internet?</h3>
    <p style="left:212px;top:135px;width:250px">A new version of Transport Layer Security (TLS) is coming...</p>
  </article>

  <article class="blog-card" style="left:609px;top:3047px;width:478px;height:202px">
    <div class="blog-img" role="img" aria-label="Server racks lit in blue and green" style="left:0;top:0;width:191px;height:202px;background:linear-gradient(135deg,#0a1f7a 0%,#1a3bd0 55%,#2c8a4a 100%)"></div>
    <span class="date" style="left:212px;top:22px">16 Dec 2020</span>
    <h3 style="left:212px;top:66px">The irony of the Corvanta<br>hack</h3>
    <p style="left:212px;top:135px;width:250px">I must confess, there was just the slightest sense of schadenfreude</p>
  </article>
</section>

<footer>
  <div class="abs footer"></div>
  <div class="abs brand" style="left:112px;top:3420px;font-size:44px;gap:14px"><span class="brand-dot" style="width:54px;height:54px"></span>quillmo</div>
  <div class="abs foot-col" style="left:439px;top:3396px;color:#fff">
    <h4>Qucik Links</h4>
    <ul><li>Home</li><li>Product</li><li>Blog</li><li>About</li><li>Partner</li><li>Contact Us</li></ul>
  </div>
  <div class="abs foot-col" style="left:656px;top:3396px;color:#fff">
    <h4>Get Connected</h4>
    <ul><li>Careers</li><li>Terms Of Service</li><li>Privacy Policy</li><li>Legal Support</li></ul>
  </div>
  <div class="abs foot-col" style="left:910px;top:3396px;color:#fff">
    <h4>Qucik Links</h4>
    <div class="contact">
      <svg width="40" height="40" viewBox="0 0 40 40"><circle cx="20" cy="20" r="18.5" fill="none" stroke="#7CC142" stroke-width="2"/><path d="M14 12c1-1 2-1 3 0l2 3c.5 1 .3 2-.5 2.6l-1 .8c1 2.2 2.8 4 5 5l.8-1c.6-.8 1.6-1 2.6-.5l3 2c1 1 1 2 0 3l-1.4 1.4c-5 1-14-8-13-13z" fill="#7CC142"/></svg>
      <div><b>Quillmo Australia:</b><span>+61 2 5550 0142</span></div>
    </div>
    <div class="contact">
      <svg width="40" height="40" viewBox="0 0 40 40"><circle cx="20" cy="20" r="18.5" fill="none" stroke="#7CC142" stroke-width="2"/><path d="M14 12c1-1 2-1 3 0l2 3c.5 1 .3 2-.5 2.6l-1 .8c1 2.2 2.8 4 5 5l.8-1c.6-.8 1.6-1 2.6-.5l3 2c1 1 1 2 0 3l-1.4 1.4c-5 1-14-8-13-13z" fill="#7CC142"/></svg>
      <div><b>Quillmo Germany:</b><span>+49 69 555 01 287</span></div>
    </div>
  </div>
  <div class="abs bottom">© 2021 Company Name. All Rights Reserved</div>
</footer>

</body>
</html>
```